RWT Installations Ltd Business Cards

We need a business card with our business logo. We provide window and door installations on high-rises in west coast British Colombia, Canada.

I would like my business information and details on one side of the card, and the other side the company name with logo

Target Market(s)

General Contractors

Industry/Entity Type

Construction

Contact Information for Business Card

one side i want my company name and logo in the dark theme logo that i provided

Requirements
Must have
• Tomas Verelund, 15559284016, RWTInstallations@mailvera.example, 1408-5192 Pellow Avenue Burnaby BC, V0X 1Z9, Owner & Manager

```html
<!DOCTYPE html>
<html lang="en">
<head>
<meta charset="utf-8">
<title>RWT Installations Ltd – Business Card</title>
<link rel="stylesheet" href="https://fonts.googleapis.com/css2?family=Poppins:wght@400;600;700&display=swap">
<style>
  :root {
    --stage: #151515;
    --card: #232323;
    --card-back: #1b1b1b;
    --accent: #29a8e0;
    --ink: #f2f2f2;
    --muted: #bfbfbf;
  }
  * { box-sizing: border-box; margin: 0; padding: 0; }
  html, body { width: 1200px; height: 900px; overflow: hidden; }
  body {
    background: var(--stage);
    font-family: "Poppins", sans-serif;
    color: var(--ink);
    position: relative;
  }
  .card {
    position: absolute;
    left: 250px;
    width: 700px;
    height: 400px;
    overflow: hidden;
    box-shadow: 0 16px 40px rgba(0,0,0,.6);
  }
  .card::after {
    content: "";
    position: absolute;
    left: 0; right: 0; bottom: 0;
    height: 8px;
    background: var(--accent);
  }
  .card--back { top: 30px; background: var(--card-back); }
  .card--front { top: 465px; background: var(--card); }

  .pattern-field {
    position: absolute;
    inset: 0 0 8px 0;
    background: linear-gradient(120deg, #141414 0%, #1f1f1f 40%, #5a5a5a 75%, #8a8a8a 100%);
    opacity: .85;
  }
  .back-brand {
    position: absolute;
    right: 40px;
    bottom: 48px;
    display: flex;
    align-items: center;
    gap: 14px;
  }
  .back-brand__square {
    flex: none;
    width: 46px;
    height: 46px;
    background: var(--accent);
  }
  .back-brand__name {
    font-weight: 600;
    font-size: 22px;
    color: var(--ink);
    white-space: nowrap;
    letter-spacing: .02em;
  }

  .brand {
    position: absolute;
    left: 40px;
    top: 118px;
    width: 290px;
    display: flex;
    align-items: center;
    gap: 16px;
  }
  .brand__square {
    flex: none;
    width: 58px;
    height: 58px;
    background: var(--accent);
  }
  .brand__name {
    font-weight: 600;
    font-size: 26px;
    line-height: 1.15;
    color: var(--ink);
    letter-spacing: .02em;
  }
  .divider {
    position: absolute;
    left: 345px;
    top: 100px;
    width: 3px;
    height: 150px;
    background: var(--accent);
  }
  .contact {
    position: absolute;
    left: 372px;
    top: 98px;
    right: 20px;
  }
  .contact__name {
    font-weight: 700;
    font-size: 28px;
    color: var(--accent);
    text-transform: uppercase;
    letter-spacing: .03em;
    line-height: 1;
  }
  .contact__role {
    font-size: 15px;
    color: var(--ink);
    margin-top: 4px;
    margin-bottom: 18px;
  }
  .contact__list { list-style: none; }
  .contact__item {
    display: flex;
    align-items: center;
    gap: 8px;
    font-size: 15px;
    line-height: 1.6;
    white-space: nowrap;
  }
  .contact__item svg { width: 14px; height: 14px; flex: none; }
  .contact__web .accent { color: var(--accent); }
  .address {
    position: absolute;
    left: 150px;
    top: 300px;
    display: flex;
    align-items: center;
    gap: 10px;
    font-size: 17px;
    white-space: nowrap;
  }
  .address svg { width: 16px; height: 18px; }
</style>
</head>
<body>

<section class="card card--back" aria-label="Card back">
  <div class="pattern-field" role="img" aria-label="Repeating company emblem pattern in glossy black and silver tones"></div>
  <div class="back-brand">
    <span class="back-brand__square" aria-hidden="true"></span>
    <span class="back-brand__name">RWT Installations Ltd</span>
  </div>
</section>

<section class="card card--front" aria-label="Card front">
  <div class="brand">
    <span class="brand__square" aria-hidden="true"></span>
    <span class="brand__name">RWT Installations Ltd</span>
  </div>

  <div class="divider" aria-hidden="true"></div>

  <div class="contact">
    <h1 class="contact__name">Tomas Verelund</h1>
    <p class="contact__role">Owner &amp; Manager</p>
    <ul class="contact__list">
      <li class="contact__item">
        <svg viewBox="0 0 24 24" fill="var(--accent)" aria-hidden="true"><path d="M6.6 10.8a15.1 15.1 0 0 0 6.6 6.6l2.2-2.2a1 1 0 0 1 1-.25 11.4 11.4 0 0 0 3.6.57 1 1 0 0 1 1 1V20a1 1 0 0 1-1 1A17 17 0 0 1 3 4a1 1 0 0 1 1-1h3.5a1 1 0 0 1 1 1c0 1.25.2 2.45.57 3.57a1 1 0 0 1-.25 1z"/></svg>
        555-928-4016
      </li>
      <li class="contact__item">
        <svg viewBox="0 0 24 24" fill="none" stroke="var(--accent)" stroke-width="2" aria-hidden="true"><rect x="3" y="5" width="18" height="14" rx="1"/><path d="M3 6l9 7 9-7"/></svg>
        RWTInstallations@mailvera.example
      </li>
      <li class="contact__item contact__web">
        <svg viewBox="0 0 24 24" fill="none" stroke="var(--accent)" stroke-width="2" aria-hidden="true"><circle cx="12" cy="12" r="9"/><path d="M3 12h18M12 3c3 3 3 15 0 18M12 3c-3 3-3 15 0 18"/></svg>
        <span>www.<span class="accent">rwtinstallations</span>.example</span>
      </li>
    </ul>
  </div>

  <p class="address">
    <svg viewBox="0 0 24 28" fill="var(--accent)" aria-hidden="true"><path d="M12 0a9 9 0 0 0-9 9c0 7 9 19 9 19s9-12 9-19a9 9 0 0 0-9-9zm0 12.5A3.5 3.5 0 1 1 12 5.5a3.5 3.5 0 0 1 0 7z"/></svg>
    1408-5192 Pellow Avenue Burnaby BC, V0X 1Z9
  </p>
</section>

</body>
</html>
```